A Healthy BRAX Louisiana- TOVL Conference Poster

LA Carewell is presenting at the TOVL conference. The TOVL is a annual meeting for State, Federal and private sector individuals to provide opportunities for the exchange of ideas related to Carewell systems and heath policy affected by those systems. Louisiana will be presenting on their LaBRAX Program . A poster with the information in the PowerPoint is needed. The first slide shows a draft of organization. The wording on slides two and three should be displayed in a visually appealing infographic. The charts should coordinate with the overall design. We would like to see the Louisiana state capital building incorporated.

Font styles to use
Sans Serif

Colors

Designer to choose colors to be used in the design.

Requirements
Must have
• Visually appealing infographics and charts
Nice to have
• Incorporate the capital building, incorporate the LaBRAX logo (on first slide)

```html
<!DOCTYPE html>
<html lang="en">
<head>
<meta charset="utf-8">
<title>A Healthy BRAX Louisiana – TOVL Conference Poster</title>
<link href="https://fonts.googleapis.com/css2?family=Oswald:wght@400;700&family=Montserrat:wght@400;600;700&display=swap" rel="stylesheet">
<style>
  :root{
    --backdrop:#c3c3c3;
    --brand-blue:#3c6ea6;
    --brand-green:#6cc12f;
    --band-blue:#3b6ea5;
    --band-green:#8dcc5b;
    --circle-blue-hi:#5b93d6;
    --circle-blue-lo:#1f5aa0;
    --circle-green-hi:#6fce35;
    --circle-green-lo:#2f8a12;
    --ribbon:#6d6f73;
    --hub-text:#5c6066;
    --white:#ffffff;
    --ink:#333b44;
  }
  *{box-sizing:border-box;margin:0;padding:0}
  html,body{width:1200px;height:1200px;overflow:hidden}
  body{background:var(--backdrop);font-family:"Montserrat",sans-serif;position:relative}
  .poster{position:absolute;left:0;top:300px;width:1200px;height:600px;overflow:hidden;background:var(--white)}
  .capitol-photo{position:absolute;inset:0;
    background:
      radial-gradient(ellipse 60% 45% at 50% 100%, rgba(70,110,60,.85), rgba(70,110,60,0) 70%),
      linear-gradient(180deg,#fbfbfd 0%,#eef0f3 25%,#c8ccd2 55%,#a9afb3 75%,#5f8a4a 92%,#4c7a3c 100%);}
  .program-name{position:absolute;left:62px;top:92px;font-family:"Montserrat",sans-serif;font-weight:700;
    font-size:40px;line-height:1;color:var(--ink)}
  .headline{position:absolute;left:0;top:0;font-family:"Oswald",sans-serif;font-weight:700;line-height:1;letter-spacing:1px;white-space:nowrap}
  .headline span{position:absolute;display:block}
  .headline-top{left:386px;top:36px;font-size:86px;color:var(--brand-green)}
  .headline-bottom{left:632px;top:112px;font-size:77px;color:var(--brand-blue)}
  .band{position:absolute;top:202px;height:53px;color:var(--white);font-size:11.2px;line-height:14px;padding:8px 42px 0}
  .band-intro{left:0;width:578px;background:var(--band-blue)}
  .band-goal{left:628px;width:572px;background:var(--band-green);padding-left:60px;padding-right:30px}
  .diagram{position:absolute;inset:0}
  .bubble{position:absolute;width:80px;height:80px;border-radius:50%;
    border:2px solid rgba(255,255,255,.9);box-shadow:0 2px 4px rgba(0,0,0,.35);
    color:var(--white);font-size:4.6px;line-height:5.6px;text-align:center;
    display:flex;align-items:center;justify-content:center;padding:18px 11px}
  .bubble.top{padding-top:24px;padding-bottom:10px}
  .bubble.bottom{padding-top:8px;padding-bottom:24px}
  .bubble-blue{background:radial-gradient(circle at 40% 30%,var(--circle-blue-hi),var(--circle-blue-lo))}
  .bubble-green{background:radial-gradient(circle at 40% 30%,var(--circle-green-hi),var(--circle-green-lo))}
  .ribbon{position:absolute;left:50%;transform:translateX(-50%);width:80px;min-height:13px;
    background:var(--ribbon);color:var(--white);font-weight:700;font-size:4.8px;line-height:5px;
    text-align:center;padding:2px 4px;
    clip-path:polygon(6% 0,94% 0,100% 50%,94% 100%,6% 100%,0 50%)}
  .bubble.top .ribbon{top:-4px}
  .bubble.bottom .ribbon{bottom:-4px}
  .hub-label{position:absolute;width:90px;text-align:center;font-family:"Oswald",sans-serif;font-weight:400;
    font-size:13px;line-height:13px;color:var(--hub-text)}
</style>
</head>
<body>
<main class="poster">
  <div class="capitol-photo" role="img" aria-label="Photograph of the Louisiana State Capitol tower rising above green trees under an overcast sky"></div>

  <div class="program-name">LaBRAX</div>

  <h1 class="headline">
    <span class="headline-top">A HEALTHY</span>
    <span class="headline-bottom">BRAX LOUISIANA</span>
  </h1>

  <p class="band band-intro">The Louisiana Coverage Assistance Plan (LaBRAX) program allows for Carewell to pay the premium costs of member’s private health insurance when cost effective for the State.</p>
  <p class="band band-goal">To increase program participation the State is implementing strategic changes to increase enrollment by 95%, resulting in an $11.2M cost savings to the State by the end of SFY23.</p>

  <svg class="diagram" width="1200" height="600" viewBox="0 0 1200 600">
    <defs>
      <linearGradient id="hubFill" x1="0" y1="0" x2="0" y2="1">
        <stop offset="0" stop-color="#ffffff"/><stop offset="1" stop-color="#d9e0ea"/>
      </linearGradient>
      <linearGradient id="knobFill" x1="0" y1="0" x2="0" y2="1">
        <stop offset="0" stop-color="#b6c1d2"/><stop offset="1" stop-color="#7e8ca3"/>
      </linearGradient>
      <linearGradient id="laptopBase" x1="0" y1="0" x2="0" y2="1">
        <stop offset="0" stop-color="#e4e6e8"/><stop offset="1" stop-color="#8c9095"/>
      </linearGradient>
    </defs>

    <g class="hub hub-obstacles">
      <path d="M113 307 L189 383 M274 307 L189 383 M113 458 L189 383 M274 467 L189 383" stroke="#555a60" stroke-width="7"/>
      <circle cx="153" cy="347" r="17" fill="url(#knobFill)"/>
      <circle cx="225" cy="347" r="17" fill="url(#knobFill)"/>
      <circle cx="153" cy="420" r="17" fill="url(#knobFill)"/>
      <circle cx="225" cy="422" r="17" fill="url(#knobFill)"/>
      <rect x="147" y="341" width="84" height="84" rx="26" fill="url(#hubFill)" stroke="#c9d2de"/>
      <line x1="232" y1="384" x2="300" y2="384" stroke="#8fa3bd" stroke-width="1.5"/>
      <path d="M300 380 L307 384 L300 388 Z" fill="#8fa3bd"/>
    </g>

    <g class="hub hub-solutions">
      <path d="M944 303 L1019 383 M1105 303 L1019 383 M944 463 L1019 383 M1105 467 L1019 383" stroke="#555a60" stroke-width="7"/>
      <circle cx="983" cy="347" r="17" fill="url(#knobFill)"/>
      <circle cx="1055" cy="347" r="17" fill="url(#knobFill)"/>
      <circle cx="983" cy="420" r="17" fill="url(#knobFill)"/>
      <circle cx="1055" cy="422" r="17" fill="url(#knobFill)"/>
      <rect x="977" y="341" width="84" height="84" rx="26" fill="url(#hubFill)" stroke="#c9d2de"/>
      <line x1="978" y1="384" x2="912" y2="384" stroke="#8fa3bd" stroke-width="1.5"/>
      <path d="M912 380 L905 384 L912 388 Z" fill="#8fa3bd"/>
    </g>

    <g class="laptop" transform="translate(309 311)">
      <rect x="40" y="0" width="168" height="111" rx="4" fill="#1d1f22"/>
      <rect x="45" y="5" width="158" height="101" fill="#ffffff"/>
      <path d="M0 112 H239 L234 122 H5 Z" fill="url(#laptopBase)"/>
      <rect x="100" y="112" width="39" height="3" rx="1.5" fill="#9a9ea3"/>
      <g class="chart" transform="translate(45 5) scale(0.985 1)">
        <text x="80" y="10" font-size="5.5" text-anchor="middle" fill="#555" font-family="Montserrat,sans-serif">LaBRAX Participation</text>
        <g stroke="#e3e3e3" stroke-width="0.5">
          <line x1="20" y1="18" x2="150" y2="18"/><line x1="20" y1="26.4" x2="150" y2="26.4"/><line x1="20" y1="34.8" x2="150" y2="34.8"/><line x1="20" y1="43.1" x2="150" y2="43.1"/><line x1="20" y1="51.5" x2="150" y2="51.5"/><line x1="20" y1="59.9" x2="150" y2="59.9"/><line x1="20" y1="68.3" x2="150" y2="68.3"/><line x1="20" y1="76.6" x2="150" y2="76.6"/><line x1="20" y1="85" x2="150" y2="85"/>
        </g>
        <g font-size="3.2" fill="#666" text-anchor="end" font-family="Montserrat,sans-serif">
          <text x="18" y="19">1600</text><text x="18" y="27.4">1400</text><text x="18" y="35.8">1200</text><text x="18" y="44.1">1000</text><text x="18" y="52.5">800</text><text x="18" y="60.9">600</text><text x="18" y="69.3">400</text><text x="18" y="77.6">200</text><text x="18" y="86">0</text>
        </g>
        <g font-size="3.2" fill="#666" text-anchor="middle" font-family="Montserrat,sans-serif">
          <text x="25" y="91">FY12</text><text x="55" y="91">FY13</text><text x="85" y="91">FY14</text><text x="115" y="91">FY15</text><text x="145" y="91">FY16</text>
          <text x="85" y="97">Fiscal Year</text>
          <text transform="translate(7 52) rotate(-90)">Number of LaBRAX Cases</text>
        </g>
        <polyline points="25,85 115,24.3 145,85" fill="none" stroke="#3a6fd0" stroke-width="1"/>
      </g>
    </g>

    <g class="laptop" transform="translate(645 311)">
      <rect x="30" y="0" width="168" height="111" rx="4" fill="#1d1f22"/>
      <rect x="35" y="5" width="158" height="101" fill="#ffffff"/>
      <path d="M0 112 H239 L234 122 H5 Z" fill="url(#laptopBase)"/>
      <rect x="100" y="112" width="39" height="3" rx="1.5" fill="#9a9ea3"/>
      <g class="chart" transform="translate(35 5) scale(0.985 1)">
        <text x="80" y="10" font-size="5.5" text-anchor="middle" fill="#555" font-family="Montserrat,sans-serif">LaBRAX Participation</text>
        <g stroke="#e3e3e3" stroke-width="0.5">
          <line x1="20" y1="18" x2="150" y2="18"/><line x1="20" y1="26.4" x2="150" y2="26.4"/><line x1="20" y1="34.8" x2="150" y2="34.8"/><line x1="20" y1="43.1" x2="150" y2="43.1"/><line x1="20" y1="51.5" x2="150" y2="51.5"/><line x1="20" y1="59.9" x2="150" y2="59.9"/><line x1="20" y1="68.3" x2="150" y2="68.3"/><line x1="20" y1="76.6" x2="150" y2="76.6"/><line x1="20" y1="85" x2="150" y2="85"/>
        </g>
        <g font-size="3.2" fill="#666" text-anchor="end" font-family="Montserrat,sans-serif">
          <text x="18" y="19">1600</text><text x="18" y="27.4">1400</text><text x="18" y="35.8">1200</text><text x="18" y="44.1">1000</text><text x="18" y="52.5">800</text><text x="18" y="60.9">600</text><text x="18" y="69.3">400</text><text x="18" y="77.6">200</text><text x="18" y="86">0</text>
        </g>
        <g font-size="3.2" fill="#666" text-anchor="middle" font-family="Montserrat,sans-serif">
          <text x="25" y="91">FY17</text><text x="49" y="91">FY19</text><text x="73" y="91">FY20</text><text x="97" y="91">FY21</text><text x="121" y="91">FY22</text><text x="145" y="91">FY23</text>
          <text x="85" y="97">Fiscal Year</text>
          <text transform="translate(7 52) rotate(-90)">Number of LaBRAX Cases</text>
        </g>
        <polyline points="25,85 49,67.4 73,62.8 97,51.5 121,41 145,26.4" fill="none" stroke="#3a6fd0" stroke-width="1"/>
        <g fill="#3a6fd0">
          <circle cx="25" cy="85" r="1"/><circle cx="49" cy="67.4" r="1"/><circle cx="73" cy="62.8" r="1"/><circle cx="97" cy="51.5" r="1"/><circle cx="121" cy="41" r="1"/><circle cx="145" cy="26.4" r="1"/>
        </g>
      </g>
    </g>
  </svg>

  <div class="hub-label" style="left:144px;top:370px">THE<br>OBSTACLES</div>
  <div class="hub-label" style="left:974px;top:370px">THE<br>SOLUTIONS</div>

  <div class="bubble bubble-blue top" style="left:73px;top:267px">
    <span class="ribbon">BUDGET CONSTRAINTS</span>
    Due to a budget shortfall the LaBRAX program ended in Dec 2015, so members paid their own premiums or moved to Carewell.
  </div>
  <div class="bubble bubble-green top" style="left:234px;top:267px">
    <span class="ribbon">LACK OF PUBLIC KNOWLEDGE</span>
    Members are unaware this program exists or find it hard to believe Carewell will pay for private health insurance.
  </div>
  <div class="bubble bubble-green bottom" style="left:73px;top:418px">
    Crowd out occurs when members choose public insurance in lieu of available private health insurance.
    <span class="ribbon">CROWD OUT</span>
  </div>
  <div class="bubble bubble-blue bottom" style="left:234px;top:427px">
    Cost effectiveness formula is too restrictive, excluding a large share of the viable population, including waiver members.
    <span class="ribbon">LACK OF PARTICIPATION</span>
  </div>

  <div class="bubble bubble-blue top" style="left:904px;top:263px">
    <span class="ribbon">PROGRAM RESTORED</span>
    LaBRAX was reinstated in April 2017, restoring the focus on employer-sponsored insurance.
  </div>
  <div class="bubble bubble-green top" style="left:1065px;top:263px">
    <span class="ribbon">INCREASE AWARENESS AND PUBLIC KNOWLEDGE</span>
    LHA has contracted a marketing firm to develop an outreach strategy aimed at providers, employers and members.
  </div>
  <div class="bubble bubble-green bottom" style="left:904px;top:423px">
    Data mining identifies individuals and populations to be targeted for program outreach.
    <span class="ribbon">DATA AND ANALYTICS</span>
  </div>
  <div class="bubble bubble-blue bottom" style="left:1065px;top:427px">
    Refining the cost effectiveness formula increased the pool of members eligible for the program, including waiver members.
    <span class="ribbon">INCREASE PARTICIPATION</span>
  </div>
</main>
</body>
</html>
```